Oil and Gas Exploration and Production company needs a business card design

We need a business card design using our logo and colors in the logo. We want a mainstream design.

```html
<!DOCTYPE html>
<html lang="en">
<head>
<meta charset="utf-8">
<title>Vela Oil &amp; Gas – Business Card</title>
<link rel="stylesheet" href="https://fonts.googleapis.com/css2?family=Alegreya+Sans+SC:wght@800&family=Tinos:wght@400;700&display=swap">
<style>
  :root {
    --backdrop: #666666;
    --card: #ffffff;
    --ink: #111111;
    --gold: #c69a34;
    --dark: #231f20;
  }
  * { margin: 0; padding: 0; box-sizing: border-box; }
  html, body { width: 900px; height: 1200px; overflow: hidden; }
  body { background: var(--backdrop); position: relative; font-family: "Tinos", "Times New Roman", serif; color: var(--ink); }

  .card {
    position: absolute; left: 88px; width: 732px; height: 429px;
    background: var(--card); border-radius: 24px; overflow: hidden;
  }
  .card--front { top: 126px; }
  .card--back { top: 641px; }

  .accent-panel { position: absolute; inset: 0; width: 100%; height: 100%; }

  .wordmark {
    position: absolute; left: 42px; top: 78px;
    font-family: "Tinos", "Times New Roman", serif; font-weight: 700;
    font-size: 40px; color: var(--ink); white-space: nowrap;
  }

  .holder-name {
    position: absolute; left: 42px; top: 196px;
    font-family: "Alegreya Sans SC", "Arial", sans-serif; font-weight: 800;
    font-size: 27px; line-height: 1; color: var(--ink);
  }
  .holder-title {
    position: absolute; left: 42px; top: 227px;
    font-weight: 700; font-size: 16px; color: var(--gold);
  }

  .contact-list { position: absolute; left: 42px; top: 264px; list-style: none; font-size: 16px; }
  .contact-list li { display: flex; align-items: center; height: 25px; }
  .contact-list svg { width: 16px; height: 16px; margin-right: 11px; fill: var(--gold); }

  .address { position: absolute; left: 42px; top: 350px; font-size: 16px; line-height: 24px; }

  .back-brand {
    position: absolute; left: 0; right: 0; top: 186px;
    display: flex; align-items: center; justify-content: center; gap: 16px;
  }
  .back-brand__dot { width: 48px; height: 48px; border-radius: 50%; background: var(--dark); }
  .back-brand__name { font-weight: 700; font-size: 52px; color: var(--ink); white-space: nowrap; }
</style>
</head>
<body>

  <section class="card card--front">
    <svg class="accent-panel" viewBox="0 0 732 429" aria-hidden="true">
      <path d="M560 0 L732 0 L732 429 L600 429 C 430 380, 420 210, 560 0 Z" fill="var(--gold)"/>
    </svg>

    <div class="wordmark">Vela Oil &amp; Gas</div>

    <h1 class="holder-name">Daniel Morrow</h1>
    <p class="holder-title">Managing Director</p>

    <ul class="contact-list">
      <li>
        <svg viewBox="0 0 16 16" aria-hidden="true"><path d="M3.5 1.5l2.3 2.6-1.2 1.6c.9 1.9 2.2 3.2 4 4l1.6-1.2 2.6 2.3-1.3 2.4c-5-.4-9.3-4.6-9.6-9.7z"/></svg>
        555.014.2280
      </li>
      <li>
        <svg viewBox="0 0 16 16" aria-hidden="true"><path d="M1 3.5h14v9H1z M2 4.5l6 4.5 6-4.5" fill="none" stroke="var(--gold)" stroke-width="1.4"/><path d="M1.5 4l6.5 5 6.5-5v8.5h-13z"/></svg>
        daniel@velaoilgas.com
      </li>
      <li>
        <svg viewBox="0 0 16 16" aria-hidden="true"><g fill="none" stroke="var(--gold)" stroke-width="1.2"><circle cx="8" cy="8" r="6.5"/><ellipse cx="8" cy="8" rx="2.8" ry="6.5"/><path d="M1.5 8h13M2.5 4.8h11M2.5 11.2h11"/></g></svg>
        www.velaoilgas.com
      </li>
    </ul>

    <address class="address" style="font-style: normal;">
      210 Ridgeline Road, Fairhaven<br>
      California 90210
    </address>
  </section>

  <section class="card card--back">
    <div class="back-brand">
      <span class="back-brand__dot" aria-hidden="true"></span>
      <span class="back-brand__name">Vela Oil &amp; Gas</span>
    </div>
  </section>

</body>
</html>
```